Acupuncture Medspa needs a business card design

I need a business card design that looks professional, has a spa-like quality and can offer a promo on the back. Initial promo is "First session free". The tagline of NeedleNook is: Refresh, Restore, Rejuvenate.

NeedleNook is a membership-based acupuncture medspa that offers acupuncture, cupping, and herbal therapies. Members choose between the "Refresh" membership which is for stress relief, or "Restore" which is for treating health conditions, and lastly "Rejuvenate" which is for natural facial enhancement.

Industry/Entity Type

Health And Wellness

Contact Information for Business Card

Coral Haskins, MAC, L.Ac.
612-555-0193
www.needlenook-example.com

Font styles to use
Serif
Sans Serif

Colors

Designer to choose colors to be used in the design.

Requirements
Must have
• The project must have NeedleNook logo, promo on the back, and contact information
Nice to have
• I would like to see the colors of the logo used.

```html
<!DOCTYPE html>
<html lang="en">
<head>
<meta charset="utf-8">
<title>NeedleNook Business Card</title>
<link href="https://fonts.googleapis.com/css2?family=Arimo:wght@400;700&display=swap" rel="stylesheet">
<style>
  :root {
    --backdrop: #dbdbdb;
    --card-white: #ffffff;
    --teal: #138b84;
    --brown: #3d2314;
    --ink: #1c1c1c;
    --ink-dark: #2b1d14;
  }
  * { margin: 0; padding: 0; box-sizing: border-box; }
  html, body {
    width: 1200px;
    height: 900px;
    overflow: hidden;
    background: var(--backdrop);
    font-family: "Arimo", Arial, sans-serif;
  }
  .canvas { position: relative; width: 1200px; height: 900px; }

  .card {
    position: absolute;
    left: 283px;
    width: 634px;
    height: 361px;
    overflow: hidden;
  }
  .card--front { top: 74px; background: var(--card-white); }
  .card--back { top: 483px; background: var(--teal); }

  /* Front */
  .wordmark {
    position: absolute;
    font-weight: 700;
    color: var(--teal);
    line-height: 1;
    white-space: nowrap;
  }
  .card--front .wordmark {
    left: 33px;
    top: 82px;
    font-size: 42px;
    letter-spacing: 0.5px;
  }
  .name-accent {
    position: absolute;
    left: 0;
    top: 174px;
    width: 16px;
    height: 49px;
    background: var(--teal);
  }
  .person-name {
    position: absolute;
    left: 33px;
    top: 168px;
    font-size: 35px;
    font-weight: 400;
    color: var(--teal);
    line-height: 1;
  }
  .credentials {
    position: absolute;
    left: 33px;
    top: 209px;
    font-size: 17px;
    color: var(--brown);
    line-height: 1;
  }
  .credentials-rule {
    position: absolute;
    left: 126px;
    right: 0;
    top: 217px;
    height: 2px;
    background: var(--teal);
  }
  .contact-list { position: absolute; left: 33px; top: 252px; }
  .contact-row {
    display: flex;
    align-items: baseline;
    height: 26px;
    font-size: 14px;
    color: var(--ink);
  }
  .contact-label { width: 64px; }
  .contact-divider { width: 20px; }
  .contact-value { font-size: 14px; }

  .footer-band {
    position: absolute;
    left: 0;
    right: 0;
    top: 311px;
    height: 26px;
  }
  .footer-band__teal {
    position: absolute; left: 0; top: 0; width: 320px; height: 100%;
    background: var(--teal);
  }
  .footer-band__brown {
    position: absolute; left: 320px; right: 0; top: 0; height: 100%;
    background: var(--brown);
  }
  .footer-band__dot {
    position: absolute;
    left: 302px;
    top: -4px;
    width: 34px;
    height: 34px;
    border-radius: 50%;
    background: var(--card-white);
    border: 2px solid var(--teal);
  }

  /* Back */
  .card--back .wordmark {
    left: 0;
    right: 0;
    top: 178px;
    text-align: center;
    font-size: 58px;
    color: var(--card-white);
    letter-spacing: 1px;
  }
  .promo {
    position: absolute;
    left: 0;
    right: 0;
    top: 313px;
    display: flex;
    align-items: center;
  }
  .promo__rule { flex: 1; height: 2px; background: var(--ink-dark); }
  .promo__text {
    padding: 0 10px;
    font-size: 21px;
    color: var(--ink-dark);
    line-height: 1;
    white-space: nowrap;
  }
</style>
</head>
<body>
<main class="canvas">
  <section class="card card--front" aria-label="Business card front">
    <div class="wordmark">NeedleNook</div>
    <div class="name-accent"></div>
    <h1 class="person-name">Coral Haskins</h1>
    <p class="credentials">MAC, L.Ac.</p>
    <div class="credentials-rule"></div>
    <div class="contact-list">
      <div class="contact-row">
        <span class="contact-label">Phone</span>
        <span class="contact-divider">I</span>
        <span class="contact-value">612-555-0193</span>
      </div>
      <div class="contact-row">
        <span class="contact-label">Website</span>
        <span class="contact-divider">I</span>
        <span class="contact-value">www.needlenook-example.com</span>
      </div>
    </div>
    <div class="footer-band">
      <div class="footer-band__teal"></div>
      <div class="footer-band__brown"></div>
      <div class="footer-band__dot"></div>
    </div>
  </section>

  <section class="card card--back" aria-label="Business card back">
    <div class="wordmark">NeedleNook</div>
    <div class="promo">
      <span class="promo__rule"></span>
      <span class="promo__text">First session free</span>
      <span class="promo__rule"></span>
    </div>
  </section>
</main>
</body>
</html>
```